A WEBSITE FOR A JEWELLERY RETAIL STORE WITH A SHOPPING CART, AND ABILITY TO ORDER ONLINE.

I require a website with a shopping cart.

We sell MAINLY diamond jewellery (such as rings etc). I need it to be simple to change prices with only a few buttons, as the price fluctuates due to the US Dollar.

We are a diamond wholesaler, selling directly to the public, so we guarantee the lowest prices in Australia.

There is also a link to current inventory that will need to be uploaded to the site.

This could be an ongoing job, where you will be paid weekly to maintain and update the website if you wish.

Target Market(s)

People getting engaged, and wanting to buy a diamond ring.

Number of Pages Required

5+ page

Colors

Designer to choose colors to be used in the design.

Requirements
Must have
• elegant.
• modern.
• professional.
• SHOPPING CART.
• ABILITY TO SEARCH FOR LOOSE DIAMONDS (LINK THAT NEEDS TO BE EMBEDDED WILL BE SENT WHICH SHOWS CURRENT STOCK).
• ENGAGEMENT RINGS
• WEDDING RINGS
• DIAMOND EARRINGS
• DIAMOND PENDANTS
• LOOSE DIAMONDS.
• SALE ITEMS.
• OTHER JEWELLERY.
• EDUCATION
• WISH LIST
• CART.
Nice to have
• a good place to look for inspiration on pages is https://www.lumenvael.example.
• YOU MAY VISIT OUR FACEBOOK PAGE AT.
• HTTP://WWW.SOCIALPAGE.EXAMPLE/QUILLSTONEJEWELLERS
Should not have
• We don't want it too busy.

```html
<!DOCTYPE html>
<html lang="en">
<head>
<meta charset="utf-8">
<title>Cart – Quillstone Jewellers Australia</title>
<link href="https://fonts.googleapis.com/css2?family=Questrial&family=Cinzel:wght@400&display=swap" rel="stylesheet">
<style>
:root{
  --ink:#1a1a1a;
  --black:#000;
  --white:#fff;
  --wine:#5a1f1f;
  --muted:#555;
  --rule:#cfcfcf;
  --taupe:#8b7665;
  --stone:#e6e6e6;
}
*{box-sizing:border-box;margin:0;padding:0}
html,body{width:1200px;height:2635px;overflow:hidden;background:var(--white)}
body{position:relative;font-family:"Questrial",sans-serif;color:var(--ink);letter-spacing:1px}
.abs{position:absolute}
a{color:inherit;text-decoration:none}

.promo-bar{left:0;top:0;width:1200px;height:57px;background:var(--black);color:var(--white);
  font-family:"Cinzel",serif;font-size:15px;letter-spacing:1px;display:flex;align-items:center;justify-content:center}

.country{left:31px;top:106px;font-size:15px;display:flex;align-items:center;gap:6px;letter-spacing:1.5px}
.country .pill{border:1px solid #777;border-radius:6px;padding:2px 12px;font-size:14px}

.brand{left:449px;top:88px;width:282px;text-align:center}
.brand-name{display:flex;align-items:center;justify-content:center;gap:10px;font-size:22px;letter-spacing:2px;color:var(--ink);height:44px}
.brand-name .mark{width:22px;height:22px;background:var(--ink)}
.brand-rule{height:3px;background:var(--wine);margin-top:6px}
.brand-tag{font-family:"Cinzel",serif;font-size:13px;letter-spacing:9px;margin-top:8px;color:#333}

.account-links{top:110px;font-size:14px;letter-spacing:1.5px;color:#333}
.account-links.register{left:826px}
.account-links.wishlist{left:978px}
.account-links.cart{left:1075px}

.rule{height:1px;background:var(--rule)}
.main-nav{left:40px;top:232px;font-size:13.5px;letter-spacing:2.5px;color:#333}
.nav-item{position:absolute;top:0;white-space:nowrap}
.search{left:892px;top:228px;width:253px;border-bottom:1px solid #888;height:20px;font-size:11px;color:#666;letter-spacing:1px}
.search svg{position:absolute;right:6px;top:0}

.crumb{left:39px;top:335px;font-size:13.5px;color:#333}
.crumb span{color:var(--wine)}
.page-title{left:0;top:380px;width:1233px;text-align:center;font-size:34px;letter-spacing:4px;color:#2a1a1a}

.col-head{top:502px;font-size:16px;letter-spacing:2px;color:#333}
.table-rule{left:39px;top:532px;width:1117px;height:1px;background:#555}

.product-photo{left:62px;width:195px;height:155px;border-radius:8px;background:radial-gradient(ellipse at center,#f2f2f2,#d8d8d8)}
.product-photo.pendant{left:110px;width:100px;height:210px;background:linear-gradient(180deg,#f5f5f5,#d6d6d6)}
.remove{right:58px;font-size:15px;color:var(--wine);text-decoration:underline;letter-spacing:1.5px}
.p-name{left:328px;font-size:17px;letter-spacing:2px}
.p-meta{left:328px;font-size:15px;letter-spacing:1.5px}
.p-price{left:609px;font-size:14px;letter-spacing:1.5px}
.qty{left:846px;width:88px;height:34px;border:1px solid #555;font-size:13px;padding:8px 14px;color:#444}
.qty svg{position:absolute;right:8px;top:10px}
.p-total{left:1058px;font-size:14px;letter-spacing:1.5px}

.gift{left:0;top:1123px;width:1276px;text-align:center;font-size:15px;color:#7a3a3a;text-decoration:underline;letter-spacing:1.5px}

.discount{left:339px;top:1190px;width:591px;height:71px;border:1px solid #444;display:flex}
.discount .field{flex:1;padding:0 14px;display:flex;align-items:center;font-size:17px;color:#777;letter-spacing:2px}
.discount .apply{width:131px;background:var(--black);color:var(--white);display:flex;align-items:center;justify-content:center;font-size:16px;letter-spacing:2px}

.continue{left:342px;top:1363px;width:584px;height:86px;background:var(--black);color:var(--white);display:flex;align-items:center;justify-content:center;font-size:35px;letter-spacing:3px}

.checkout{left:184px;top:1521px;width:872px;height:664px;border:1px solid #777}
.label{font-size:16px;letter-spacing:2px;color:#222}
.select{left:576px;top:1584px;width:260px;height:40px;border:1px solid #777;font-size:16px;color:#999;padding:9px 20px;letter-spacing:2px}
.select svg{position:absolute;right:12px;top:14px}
.radio{left:412px;width:12px;height:12px;border-radius:50%;background:#ccc;border:1px solid #999}
.option{left:452px;font-size:17px;letter-spacing:2px;color:#333}
.pay{left:466px;width:341px;height:34px;background:var(--black);color:var(--white);font-size:16px;letter-spacing:2px;display:flex;align-items:center;justify-content:center}

.newsletter{left:0;top:2254px;width:1200px;height:80px;background:var(--taupe)}
.nl-title{font-family:"Cinzel",serif;font-size:19px;color:var(--white);letter-spacing:2px;top:28px}
.nl-input{left:228px;top:19px;width:264px;height:37px;background:var(--white);font-size:13px;color:#888;padding:10px 7px;letter-spacing:1px}
.nl-btn{left:492px;top:19px;width:132px;height:37px;background:var(--black);color:var(--white);font-family:"Cinzel",serif;font-size:13px;display:flex;align-items:center;justify-content:center;letter-spacing:1px}
.social{top:26px;width:22px;height:22px;border-radius:50%;background:#1a1a1a}

.footer{left:0;top:2334px;width:1200px;height:301px;background:var(--black);color:var(--white)}
.about{left:39px;top:40px;width:300px;font-size:13px;line-height:16px;text-align:justify;letter-spacing:.6px}
.help{left:41px;top:203px;font-size:10px;letter-spacing:1px}
.contact{left:53px;font-size:10px;letter-spacing:1px;display:flex;align-items:center;gap:6px}
.f-col{top:46px;font-size:13px;letter-spacing:1.2px}
.f-col h4{font-weight:400;font-size:15px;text-decoration:underline;margin-bottom:12px}
.f-col li{list-style:none;height:25px}
.copyright{left:0;top:2578px;width:1214px;text-align:center;font-size:13px;color:var(--white);letter-spacing:1px}
</style>
</head>
<body>

<div class="abs promo-bar">ORDER NOW AND ENJOY FREE SWIFTPOST® OVERNIGHT SHIPPING AND 30-DAY RETURNS</div>

<div class="abs country">Select your country: <span class="pill">$AUD ▾</span></div>

<div class="abs brand">
  <div class="brand-name"><span class="mark"></span>QUILLSTONE JEWELLERS</div>
  <div class="brand-rule"></div>
  <div class="brand-tag">AUSTRALIA</div>
</div>

<a class="abs account-links register" href="#">Register | Sign In</a>
<a class="abs account-links wishlist" href="#">Wishlist ♥</a>
<a class="abs account-links cart" href="#">Cart 🛒︎ (0)</a>

<div class="abs rule" style="left:0;top:206px;width:1200px"></div>
<nav class="abs main-nav">
  <span class="nav-item" style="left:0">DIAMONDS</span>
  <span class="nav-item" style="left:139px">ENGAGEMENT RINGS</span>
  <span class="nav-item" style="left:359px">WEDDING</span>
  <span class="nav-item" style="left:479px">JEWELRY</span>
  <span class="nav-item" style="left:605px">EDUCATION</span>
  <span class="nav-item" style="left:743px">ON SALE</span>
</nav>
<div class="abs search">Search
  <svg width="18" height="14" viewBox="0 0 18 14"><circle cx="6" cy="6" r="4.5" fill="none" stroke="#555" stroke-width="1.2"/><line x1="9.5" y1="9" x2="16" y2="13" stroke="#555" stroke-width="1.2"/></svg>
</div>
<div class="abs rule" style="left:0;top:296px;width:1200px"></div>

<div class="abs crumb">Home &gt;&gt; <span>Cart</span></div>
<h1 class="abs page-title" style="font-weight:400">CART</h1>

<div class="abs col-head" style="left:157px">ITEM</div>
<div class="abs col-head" style="left:585px">ITTEM PRICE</div>
<div class="abs col-head" style="left:835px">QUANTITY</div>
<div class="abs col-head" style="left:1075px">TOTAL</div>
<div class="abs table-rule"></div>

<!-- cart line 1 -->
<div class="abs product-photo" style="top:614px" role="img" aria-label="Oval halo diamond engagement ring"></div>
<a class="abs remove" href="#" style="top:580px">Remove</a>
<div class="abs p-name" style="top:621px">Product Name</div>
<div class="abs p-meta" style="top:687px">Item Code: #######</div>
<div class="abs p-price" style="top:686px">AUD XXXXX</div>
<div class="abs qty" style="top:675px">1<svg width="12" height="11" viewBox="0 0 12 11"><path d="M1 1h10L6 10z" fill="none" stroke="#555"/></svg></div>
<div class="abs p-total" style="top:686px">AUD XXXXX</div>
<div class="abs p-meta" style="top:754px">Stock : In stock</div>

<!-- cart line 2 -->
<div class="abs product-photo pendant" style="top:852px" role="img" aria-label="Diamond teardrop pendant on chain"></div>
<a class="abs remove" href="#" style="top:866px">Remove</a>
<div class="abs p-name" style="top:907px">Product Name</div>
<div class="abs p-meta" style="top:973px">Item Code: #######</div>
<div class="abs p-price" style="top:972px">AUD XXXXX</div>
<div class="abs qty" style="top:961px">1<svg width="12" height="11" viewBox="0 0 12 11"><path d="M1 1h10L6 10z" fill="none" stroke="#555"/></svg></div>
<div class="abs p-total" style="top:972px">AUD XXXXX</div>
<div class="abs p-meta" style="top:1040px">Stock : In stock</div>

<a class="abs gift" href="#">Choose Gift Wrap and Message</a>

<div class="abs discount">
  <div class="field">Enter &nbsp;Discount Code Here</div>
  <div class="apply">APPLY</div>
</div>

<a class="abs continue" href="#">Continue Shopping</a>

<section class="abs checkout"></section>
<div class="abs label" style="left:407px;top:1600px">DELIVER TO :</div>
<div class="abs select">Australia<svg width="12" height="11" viewBox="0 0 12 11"><path d="M1 1h10L6 10z" fill="none" stroke="#555"/></svg></div>
<div class="abs label" style="left:407px;top:1680px">SHIPPING METHOD :</div>
<div class="abs radio" style="top:1726px"></div>
<div class="abs option" style="top:1721px">Home delivery</div>
<svg class="abs" style="left:590px;top:1718px" width="46" height="26" viewBox="0 0 46 26" aria-hidden="true">
  <rect x="6" y="3" width="24" height="15" fill="#111"/><path d="M30 7h8l5 6v5H30z" fill="#111"/>
  <circle cx="13" cy="21" r="3.5" fill="#111"/><circle cx="37" cy="21" r="3.5" fill="#111"/>
  <line x1="0" y1="7" x2="5" y2="7" stroke="#111"/><line x1="1" y1="11" x2="5" y2="11" stroke="#111"/>
</svg>
<div class="abs radio" style="top:1779px"></div>
<div class="abs option" style="top:1774px">Click and Collect</div>
<svg class="abs" style="left:624px;top:1763px" width="26" height="34" viewBox="0 0 26 34" aria-hidden="true">
  <path d="M13 2a9 9 0 0 0-9 9c0 7 9 16 9 16s9-9 9-16a9 9 0 0 0-9-9z" fill="#111"/><circle cx="13" cy="11" r="3.5" fill="#fff"/>
  <ellipse cx="13" cy="30" rx="10" ry="2.5" fill="none" stroke="#111" stroke-width="1.5"/>
</svg>
<div class="abs label" style="left:407px;top:1864px">DELIVERY CHARGE:</div>
<div class="abs label" style="left:766px;top:1864px">AUD XX</div>
<a class="abs pay" href="#" style="top:1961px">PAYMENT OPTION 1</a>
<a class="abs pay" href="#" style="top:2025px">PAYMENT OPTION 2</a>
<a class="abs pay" href="#" style="top:2089px">PAYMENT OPTION 3</a>

<section class="abs newsletter">
  <div class="abs nl-title" style="left:38px">STAY IN TOUCH</div>
  <div class="abs nl-input">Please enter your email address</div>
  <div class="abs nl-btn">SIGN UP</div>
  <div class="abs nl-title" style="left:716px">OUR SOCIAL SIDE</div>
  <span class="abs social" style="left:962px" role="img" aria-label="Social network link"></span>
  <span class="abs social" style="left:1023px" role="img" aria-label="Social network link"></span>
  <span class="abs social" style="left:1093px" role="img" aria-label="Social network link"></span>
</section>

<footer class="abs footer">
  <p class="abs about">Lorem ipsum dolor sit amet, consectetur adipisicing elit, sed do eiusmod tempor incididunt ut labore et dolore magna aliqua. Ut enim ad minim veniam, quis nostrud exercitation ullamco laboris nisi ut aliquip ex ea commodo consequat. Duis aute irure dolor in reprehenderit in voluptate velit esse cillum dolore eu fugiat nulla pariatur. Excepteur sint occaecat</p>
  <div class="abs help">Need Help?</div>
  <div class="abs contact" style="top:225px">
    <svg width="9" height="9" viewBox="0 0 10 10"><path d="M2 1l2 2-1 1.5c.8 1.5 1.8 2.5 3.3 3.3L7.8 6.8l2 2L8.5 10C4 9.5.5 6 0 1.5z" fill="#fff"/></svg>+61-000-444-555-666</div>
  <div class="abs contact" style="top:242px">
    <svg width="9" height="7" viewBox="0 0 10 7"><rect width="10" height="7" fill="#fff"/><path d="M0 0l5 4 5-4" fill="none" stroke="#000"/></svg>hello@quillstone.example</div>
  <div class="abs f-col" style="left:571px"><h4>Account</h4><ul><li>Sign up for an account</li><li>Terms and Conditions</li><li>Privacy Policy</li><li>Site Map</li></ul></div>
  <div class="abs f-col" style="left:783px"><h4>About Us</h4><ul><li>Our Story</li><li>Gift Wrap</li><li>Jewellery Care</li><li>Engraving</li></ul></div>
  <div class="abs f-col" style="left:965px"><h4>Shopping Online</h4><ul><li>Contact Us</li><li>Australia Delivery</li><li>International Delivery</li><li>Returns</li></ul></div>
</footer>
<div class="abs copyright">© 2018 Quillstone Jewellers Australia</div>

</body>
</html>
```